NEW VSK Chatterbook and Display ADS!

We need to do Social Media designs for Valdor School of Skilled Trades
Site URL: http://www.valdorcampus.example/
Chatterbook URL: https://www.facebook.com/VSKschoolofskilledtrades/
Sizes Required
-1200x628 (Chatterbook Link Post) No more than 20% text coverage - Quantity (2)
-600x600 (Chatterbook Carousel Post) No more than 20% text coverage - Quantity (2 sets, 3 pictures)
Display Sizes: ( 2 sets)
160 x 600
300 x 50
300 x 250
300 x 600
320 x 50
728 x 90
Client is looking to focus more on the end goal of going to a trade school, not going back to school.
The ads should focus on the benefit of attending a trade school.
Watch these two videos to discover some of the inspiration for the campaign:
http://tomvashel.example/2017/03/attn-again-a-4-yr-degree-is-not-the-best-path-for-all/
here is the video:
https://www.chatterbook.example/PeterMangoHolt/videos/20865433135017623/
Please note that we cannot have more than 20% text on the image, see Chatterbook's guidelines here.
https://www.chatterbook.example/policies/ads#text_in_images

```html
<!DOCTYPE html>
<html lang="en">
<head>
<meta charset="utf-8">
<title>Valdor School of Skilled Trades – Scholarship Opportunity</title>
<link href="https://fonts.googleapis.com/css2?family=Oswald:wght@400;500;600&display=swap" rel="stylesheet">
<style>
  :root {
    --bg-dark: #141414;
    --bg-mid: #2f2f2f;
    --accent-blue: #56c8f2;
    --teal: #1a85a5;
    --teal-dark: #126a85;
    --white: #ffffff;
    --photo-orange: #d2561c;
    --photo-glow: #9fd6ff;
  }
  html, body {
    margin: 0;
    padding: 0;
    width: 1200px;
    height: 628px;
    overflow: hidden;
    background: var(--bg-dark);
  }
  .ad {
    position: relative;
    width: 1200px;
    height: 628px;
    overflow: hidden;
    font-family: "Oswald", sans-serif;
    color: var(--white);
    background:
      radial-gradient(ellipse at 30% 45%, var(--bg-mid) 0%, #1d1d1d 45%, var(--bg-dark) 80%);
  }
  .hero-photo {
    position: absolute;
    left: 440px;
    top: 0;
    width: 760px;
    height: 568px;
    background:
      radial-gradient(circle at 30% 88%, var(--white) 0%, var(--photo-glow) 6%, rgba(80,150,220,0.5) 16%, transparent 30%),
      radial-gradient(circle at 28% 12%, rgba(70,150,230,0.8) 0%, transparent 22%),
      linear-gradient(120deg, #1a1a1a 0%, #5a2410 35%, var(--photo-orange) 60%, #e8743a 80%, #8a3410 100%);
    -webkit-mask-image: linear-gradient(90deg, transparent 0%, #000 25%);
    mask-image: linear-gradient(90deg, transparent 0%, #000 25%);
  }
  .brand {
    position: absolute;
    left: 36px;
    top: 46px;
    width: 170px;
    height: 70px;
    display: flex;
    align-items: center;
    justify-content: center;
    text-align: center;
    background: var(--white);
    color: var(--teal-dark);
    font-weight: 600;
    font-size: 17px;
    line-height: 1.1;
    text-transform: uppercase;
    padding: 0 8px;
    box-sizing: border-box;
  }
  .headline {
    position: absolute;
    left: 30px;
    top: 188px;
    margin: 0;
    font-weight: 500;
    font-size: 46px;
    line-height: 1.2;
    color: var(--accent-blue);
    letter-spacing: 0.5px;
  }
  .event-line {
    position: absolute;
    left: 30px;
    top: 250px;
    margin: 0;
    font-weight: 500;
    font-size: 27px;
    letter-spacing: 0.5px;
  }
  .event-line sup { font-size: 15px; }
  .categories {
    position: absolute;
    left: 30px;
    top: 336px;
    margin: 0;
    font-weight: 500;
    font-size: 22px;
    line-height: 1.3;
    letter-spacing: 0.5px;
  }
  .contact-button {
    position: absolute;
    left: 34px;
    top: 498px;
    width: 196px;
    height: 38px;
    display: flex;
    align-items: center;
    justify-content: center;
    color: var(--white);
    text-decoration: none;
    font-family: "Oswald", sans-serif;
    font-size: 18px;
  }
  .contact-button::before {
    content: "";
    position: absolute;
    inset: 0;
    background: var(--teal);
    transform: skewX(-20deg);
    z-index: 0;
  }
  .contact-button span { position: relative; }
  .info-bar {
    position: absolute;
    left: 0;
    bottom: 0;
    width: 1200px;
    height: 60px;
    background: var(--teal);
    display: flex;
    align-items: center;
    padding: 0 38px;
    box-sizing: border-box;
    gap: 14px;
    font-size: 20px;
    letter-spacing: 0.3px;
  }
  .info-item { display: flex; align-items: center; gap: 16px; white-space: nowrap; }
  .info-item + .info-item { margin-left: 22px; }
  .info-item svg { width: 24px; height: 24px; fill: var(--white); flex: none; }
</style>
</head>
<body>
  <main class="ad">
    <div class="hero-photo" role="img" aria-label="Welder in orange protective jacket and blue welding helmet, sparks flying from the torch"></div>

    <div class="brand">Valdor School of Skilled Trades</div>

    <h1 class="headline">SCHOLARSHIP OPPORTUNITY</h1>
    <p class="event-line">WELDING COPPETITION SATURDAY APRITL 22<sup>ND</sup></p>
    <p class="categories">HIGH SCHOOL SENIOR COMPETITION<br>&amp; ADULT COMPETITION</p>

    <a class="contact-button" href="http://www.valdorcampus.example/"><span>CONTACT US</span></a>

    <footer class="info-bar">
      <div class="info-item">
        <svg viewBox="0 0 24 24" aria-hidden="true"><path d="M12 2a10 10 0 1 0 0 20 10 10 0 0 0 0-20zm6.9 6h-2.9a15.7 15.7 0 0 0-1.4-3.6A8 8 0 0 1 18.9 8zM12 4c.8 1.2 1.5 2.5 1.9 4h-3.8c.4-1.5 1.1-2.8 1.9-4zM4.3 14a8.2 8.2 0 0 1 0-4h3.4a16.5 16.5 0 0 0 0 4H4.3zm.8 2h2.9c.3 1.3.8 2.5 1.4 3.6A8 8 0 0 1 5.1 16zM8 8H5.1a8 8 0 0 1 4.3-3.6C8.8 5.5 8.3 6.7 8 8zm4 12c-.8-1.2-1.5-2.5-1.9-4h3.8c-.4 1.5-1.1 2.8-1.9 4zm2.3-6H9.7a14.7 14.7 0 0 1 0-4h4.6a14.7 14.7 0 0 1 0 4zm.3 5.6c.6-1.1 1.1-2.3 1.4-3.6h2.9a8 8 0 0 1-4.3 3.6zm1.7-5.6a16.5 16.5 0 0 0 0-4h3.4a8.2 8.2 0 0 1 0 4h-3.4z"/></svg>
        <span>www.valdorcampus.example</span>
      </div>
      <div class="info-item">
        <svg viewBox="0 0 24 24" aria-hidden="true"><path d="M12 2a7 7 0 0 0-7 7c0 5.2 7 13 7 13s7-7.8 7-13a7 7 0 0 0-7-7zm0 9.5A2.5 2.5 0 1 1 12 6.5a2.5 2.5 0 0 1 0 5z"/></svg>
        <span>218 HARLAN AVE, SUITE 4B BROOKMERE, IL 60999</span>
      </div>
      <div class="info-item">
        <svg viewBox="0 0 24 24" aria-hidden="true"><path d="M6.6 10.8a15.1 15.1 0 0 0 6.6 6.6l2.2-2.2a1 1 0 0 1 1-.24 11.4 11.4 0 0 0 3.6.57 1 1 0 0 1 1 1V20a1 1 0 0 1-1 1A17 17 0 0 1 3 4a1 1 0 0 1 1-1h3.5a1 1 0 0 1 1 1c0 1.25.2 2.45.57 3.57a1 1 0 0 1-.25 1z"/></svg>
        <span>555-014-2290</span>
      </div>
    </footer>
  </main>
</body>
</html>
```